Ferncrest Dental, LLC business card project

Business card to be designed with current logo.
Dental office- please keep design of card that looks clean and professional.
Please include the following info:
Ferncrest Dental, LLC
Dr. Lorna Pettigrew
2871 Marlowe Street
Alderbrook, OR 97399
555-555-0193
ferncrestdental.office@examplemail.test
Hello everyone-
Reason: Just got back from overseas- will look at all designs and provide feedback. Thank you!
Reason: Polling my friends for the final selection-
thank you to all those that participated- so many talented designers!

```html
<!DOCTYPE html>
<html lang="en">
<head>
<meta charset="utf-8">
<title>Ferncrest Dental, LLC – Business Card</title>
<link rel="stylesheet" href="https://fonts.googleapis.com/css2?family=Marcellus+SC&display=swap">
<style>
  :root {
    --backdrop: #4d8a43;
    --card: #ffffff;
    --brand-green: #8dbb3e;
    --ink-green: #4f8a4f;
  }
  html, body {
    margin: 0;
    padding: 0;
    width: 1200px;
    height: 658px;
    overflow: hidden;
    background: var(--backdrop);
  }
  .canvas {
    position: relative;
    width: 1200px;
    height: 658px;
    background: var(--backdrop);
  }
  .business-card {
    position: absolute;
    left: 34px;
    top: 34px;
    width: 1130px;
    height: 582px;
    background: var(--card);
  }
  .brand {
    position: absolute;
    left: 84px;
    top: 66px;
    display: flex;
    align-items: center;
    gap: 28px;
  }
  .brand-mark {
    width: 76px;
    height: 76px;
    display: block;
  }
  .brand-name {
    font-family: "Marcellus SC", serif;
    font-size: 86px;
    line-height: 1;
    color: var(--brand-green);
    font-weight: 400;
    letter-spacing: 1px;
    white-space: nowrap;
  }
  .contact {
    position: absolute;
    left: 235px;
    top: 292px;
    width: 800px;
    margin: 0;
    text-align: center;
    font-family: "Marcellus SC", serif;
    font-size: 36px;
    line-height: 52px;
    color: var(--ink-green);
    font-style: normal;
    white-space: nowrap;
  }
  .contact span { display: block; }
  .contact .email { font-size: 30px; }
</style>
</head>
<body>
<main class="canvas">
  <section class="business-card">
    <header class="brand">
      <svg class="brand-mark" viewBox="0 0 76 76" aria-hidden="true">
        <circle cx="38" cy="38" r="36" fill="var(--brand-green)"/>
      </svg>
      <span class="brand-name">Ferncrest Dental</span>
    </header>
    <address class="contact">
      <span class="person">Dr. Lorna Pettigrew</span>
      <span class="street">2871 Marlowe Street</span>
      <span class="city">Alderbrook, OR 97399</span>
      <span class="phone">Ph - 555-555-0193</span>
      <span class="email">ferncrestdental.office@examplemail.test</span>
    </address>
  </section>
</main>
</body>
</html>
```